Bellucari Wine label**

Hi, we need a design for a white, red and sparkling wine label. We are a small italian restaurant (Bellucari) and we want to release some wines under our personal brand. The restaurant has a rustic, italian provance style with with a slight modern, clean lines look. We would like a design that represent our mission to provide as authentic Italian food as we can, something that feels that it has been brought from the heart of Italy.
https://www.bellucaricafe.example/

```html
<!DOCTYPE html>
<html lang="en">
<head>
<meta charset="UTF-8">
<title>Bellucari Red Wine Label</title>
<link rel="stylesheet" href="https://fonts.googleapis.com/css2?family=Cinzel:wght@700;900&family=Great+Vibes&family=Montserrat:wght@500&display=swap">
<style>
  :root {
    --backdrop: #e5e6e7;
    --paper: #f3f1ec;
    --paper-edge: #e8e5de;
    --ink: #23221d;
    --wine-red: #b8222f;
    --gold: #c98f1c;
    --gold-light: #e7c77a;
    --stone: #d9d5cb;
  }
  * { margin: 0; padding: 0; box-sizing: border-box; }
  html, body {
    width: 1200px;
    height: 1114px;
    overflow: hidden;
    background: var(--backdrop);
  }
  .canvas {
    position: relative;
    width: 1200px;
    height: 1114px;
    display: flex;
    align-items: center;
    justify-content: center;
  }
  .label {
    position: relative;
    width: 682px;
    height: 1040px;
    background: linear-gradient(90deg, var(--paper-edge) 0%, var(--paper) 12%, var(--paper) 88%, var(--paper-edge) 100%);
    text-align: center;
    color: var(--ink);
  }
  .label__artwork {
    position: absolute;
    left: 96px;
    top: 88px;
    width: 490px;
    height: 472px;
    background:
      radial-gradient(ellipse 30% 42% at 50% 58%, var(--gold-light) 0%, rgba(231,199,122,0.35) 60%, rgba(231,199,122,0) 100%),
      radial-gradient(ellipse 60% 60% at 50% 55%, var(--stone) 0%, rgba(217,213,203,0) 100%);
    border-radius: 40% 40% 6px 6px / 30% 30% 6px 6px;
  }
  .label__name {
    position: absolute;
    left: 0;
    right: 0;
    top: 606px;
    font-family: "Cinzel", serif;
    font-weight: 900;
    font-size: 60px;
    letter-spacing: 2px;
    line-height: 1;
  }
  .label__variety {
    position: absolute;
    left: 0;
    right: 0;
    top: 716px;
    font-family: "Great Vibes", cursive;
    font-size: 46px;
    color: var(--wine-red);
    line-height: 1;
  }
  .label__description {
    position: absolute;
    left: 0;
    right: 0;
    top: 812px;
    font-family: "Montserrat", sans-serif;
    font-weight: 500;
    font-size: 16.5px;
    letter-spacing: 1.6px;
    line-height: 24px;
    text-transform: uppercase;
  }
  .label__maker {
    position: absolute;
    left: 0;
    right: 0;
    top: 918px;
    display: flex;
    flex-direction: column;
    align-items: center;
    gap: 14px;
  }
  .label__maker-dot {
    width: 38px;
    height: 38px;
    border: 2px solid var(--gold);
    border-radius: 50%;
  }
  .label__maker-name {
    font-family: "Montserrat", sans-serif;
    font-weight: 500;
    font-size: 20px;
    letter-spacing: 6px;
    color: var(--gold);
    line-height: 1;
  }
</style>
</head>
<body>
  <main class="canvas">
    <article class="label">
      <div class="label__artwork" role="img" aria-label="Engraved illustration of an arched Italian stone window with golden lattice panes, framed by climbing grapevines"></div>
      <h1 class="label__name">Bellucari</h1>
      <p class="label__variety">Red Wine</p>
      <p class="label__description">
        Quality red wine made with precision<br>
        to satisfy your taste senses,<br>
        combined with delicious Italian cuisine
      </p>
      <div class="label__maker">
        <span class="label__maker-dot"></span>
        <span class="label__maker-name">bellucari</span>
      </div>
    </article>
  </main>
</body>
</html>
```